Webdesign für Augenarztpraxis gesucht
Zielgruppe
Augenarztpraxis, Zielgruppe: Patienten, Interessenten
Aufgabenstellung
Liebe Designer, liebe Designerinnen,
es handelt sich hierbei um keinen Design-Contest, eher um eine Ausschreibung.
anbei die konkrete Projektinalte:
- bestehende HP http://www.sehzentrum-lindmoor.de moderner gestalten
- Aufbau und Inhalte können übernommen werden, nur Austausch von alten Bildern (Fotoshooting geplant)
- ergänzend: Bildlizenzen / Stockfotografie
- Aufbau aller Seiten und Unterseiten
- SEO/SEA Googleanpassungen – Implementierung relevanter Suchbegriffe
- eventuell kleine Textanpassungen
- gehostetes CMS, geringe Wartungskosten
- DSGVO konformes Impressum und Datenschutzseite
- Technische Abwicklung mit dem Hoster
Bitte um Nennung der Kosten (siehe oben):
- Gesamtkosten Umgestaltung der HP
- Kosten CMS Hosting
- sonstige Wartungskosten
- Stundensatz für sonstige Programmierleistungen
- Stundensatz für das Sichten der gelieferten Texte, anpassen und Neuanpassung der Texte pro Seite
Wichtig: bitte geben Sie Referenzen an, um die Vorauswahl zu erleichtern
Vielen Dank!
brunowaldau@postfeld.de
- es soll die bestehende HP: http://blickhaus-falkenau.de/team.html moderner gestaltet werden
- die meißten Inhalte können von der aktuellen HP: http://blickhaus-falkenau.de/team.html übernommen werden
- neue Praxis- und Mitarbeiterfotos werden durch einen Fotografen neu erstellt (Auftrag ist noch zu vergeben)
- Wichtig: bitte geben Sie unbedingt Referenzen an, um die Vorauswahl zu erleichtern
- bitte auch um die Angabe von Preisen für spätere Änderungen bezügl. Inhalte und Aufbau

```html
<!DOCTYPE html>
<html lang="de">
<head>
<meta charset="utf-8">
<title>Augenklinik Lindmoor</title>
<link rel="stylesheet" href="https://fonts.googleapis.com/css2?family=Fira+Sans+Condensed:wght@300;400;500;600;700&family=Fira+Sans:wght@500&display=swap">
<style>
:root{
  --teal:#35b7c5;
  --teal-box:rgba(53,183,197,.82);
  --ink:#3d3d3d;
  --grey:#555;
  --hero-a:#3f4c52;
  --hero-b:#6d7c82;
  --photo:#d6d8d9;
  --white:#fff;
}
*{margin:0;padding:0;box-sizing:border-box}
html,body{width:695px;height:1200px;overflow:hidden;background:var(--white)}
body{position:relative;font-family:"Fira Sans Condensed",sans-serif;color:var(--ink)}
.abs{position:absolute}

.site-header{position:absolute;left:0;top:0;width:695px;height:58px;background:var(--white)}
.brand{position:absolute;left:18px;top:13px;display:flex;align-items:center;gap:6px}
.brand-text{font-weight:600;font-size:10.5px;color:#222;line-height:1}
.brand-sub{font-weight:400;font-size:5.2px;color:#222;line-height:7px;text-align:right;margin-top:3px}
.brand-dot{width:14px;height:14px;border-radius:50%;background:var(--teal);margin-top:12px}
.nav{position:absolute;top:21px;font-weight:300;font-size:11px;letter-spacing:.9px;color:#444}
.btn-appointment{position:absolute;left:552px;top:16px;width:128px;height:22px;background:var(--teal);color:var(--white);font-weight:400;font-size:11px;letter-spacing:.9px;text-align:center;line-height:22px}

.hero{position:absolute;left:0;top:58px;width:695px;height:350px;background:linear-gradient(110deg,var(--hero-b),var(--hero-a) 55%,#56646a)}
.hero-title{position:absolute;left:58px;top:102px;color:var(--white);font-size:35px;line-height:40px;font-weight:300;text-transform:uppercase}
.hero-title b{font-weight:600}
.hours{position:absolute;left:380px;top:87px;width:281px;height:147px;background:var(--teal-box);color:var(--white)}
.hours-head{position:absolute;left:43px;top:14px;display:flex;align-items:center;gap:8px;font-weight:400;font-size:20px;letter-spacing:1.5px}
.hours-rule{position:absolute;left:21px;top:56px;width:239px;height:1px;background:var(--white)}
.hours-row{position:absolute;left:26px;font-size:14px;letter-spacing:1px;font-weight:300}
.hours-time{position:absolute;left:147px;font-family:"Fira Sans",sans-serif;font-weight:500;font-size:14px;letter-spacing:1px}

.intro-title{position:absolute;left:0;top:427px;width:695px;text-align:center;color:var(--teal);font-weight:500;font-size:14px}
.intro-text{position:absolute;left:84px;top:454px;width:510px;text-align:center;font-size:9.6px;line-height:13px;font-weight:300;color:#444}

.section-title{position:absolute;left:0;width:695px;text-align:center;font-weight:600;font-size:27px}
.services-title{top:532px;color:var(--teal)}
.service{position:absolute;top:600px;width:90px;text-align:center}
.service svg{display:block;margin:0 auto}
.service-label{margin-top:12px;font-weight:300;font-size:11px;line-height:14px;letter-spacing:1.1px;color:#555}

.team{position:absolute;left:0;top:722px;width:695px;height:437px;background:var(--teal);color:var(--white)}
.team-title{top:30px;color:var(--white)}
.team-text{position:absolute;left:60px;top:73px;width:575px;text-align:center;font-size:9.8px;line-height:13px;font-weight:300}
.member{position:absolute;width:110px;text-align:center}
.member-photo{width:108px;height:108px;margin:0 auto;background:linear-gradient(180deg,#e2e3e4,#c9cbcc)}
.member-name{margin-top:8px;font-weight:500;font-size:10.4px;line-height:12.5px}
.member-role{font-weight:300;font-size:10.4px;line-height:12.5px}
</style>
</head>
<body>

<header class="site-header">
  <div class="brand">
    <div>
      <div class="brand-text">AUGENKLINIK LINDMOOR</div>
      <div class="brand-sub">PRIV.-DOZ. DR. ANSELM KRAUTH<br>DR. HELGA BRENNECKE<br>DR. MARLENE KRAUTH</div>
    </div>
    <div class="brand-dot"></div>
  </div>
  <span class="nav" style="left:205px">LEISTUNGEN</span>
  <span class="nav" style="left:282px">DIAGNOSEN</span>
  <span class="nav" style="left:358px">BIOGRAPHIE</span>
  <span class="nav" style="left:440px">TEAM</span>
  <span class="nav" style="left:491px">KONTAKT</span>
  <a class="btn-appointment">TERMIN VEREINBAREN</a>
</header>

<section class="hero" role="img" aria-label="Foto: Ärztin misst einem Patienten am Schreibtisch den Blutdruck, mit Stethoskop und Klemmbrett">
  <h1 class="hero-title">Klinik für<br><b>Augenheilkunde</b><br>in Lindmoor</h1>
  <div class="hours">
    <div class="hours-head">
      <svg width="34" height="34" viewBox="0 0 34 34" fill="none" stroke="#fff" stroke-width="2.2">
        <rect x="2" y="5" width="24" height="20" rx="2"/>
        <line x1="2" y1="11" x2="26" y2="11"/>
        <line x1="8" y1="2" x2="8" y2="7"/><line x1="20" y1="2" x2="20" y2="7"/>
        <rect x="6" y="14" width="3" height="3" fill="#fff"/><rect x="12" y="14" width="3" height="3" fill="#fff"/>
        <rect x="6" y="19" width="3" height="3" fill="#fff"/>
        <circle cx="25" cy="25" r="7" fill="var(--teal)"/>
        <polyline points="25,21 25,25 28,25"/>
      </svg>
      <span>ÖFFNUNGSZEITEN</span>
    </div>
    <div class="hours-rule"></div>
    <div class="hours-row" style="top:79px">MO.-FR.</div>
    <div class="hours-time" style="top:79px">08:00 - 12:00 UHR</div>
    <div class="hours-row" style="top:101px">MO. DI. MI. DO.</div>
    <div class="hours-time" style="top:101px">15:00 - 17:00 UHR</div>
  </div>
</section>

<h2 class="intro-title">PRAXIS UND OPERATIONSZENTRUM - VON DER EXAKTEN DIAGNOSE ZUR BESTMÖGLICHEN THERAPIE.</h2>
<p class="intro-text">Seit 1993 besteht unser ambulantes Operationszentrum, in dieser Zeit haben wir weit über 55.000 Operationen in höchster Qualität und mit modernster Technik durchgeführt. Oberstes Ziel ist die Zufriedenheit unserer Patienten. Nach ausführlicher Diagnostik mit modernsten Geräten und individueller Beratung werden ambulante Operationen und Behandlungen in einem breiten Spektrum durchgeführt. Vereinbaren Sie mit uns ein persönliches Beratungsgespräch.</p>

<h2 class="section-title services-title">UNSERE LEISTUNGEN</h2>

<div class="service" style="left:42px">
  <svg width="36" height="36" viewBox="0 0 36 36" fill="none" stroke="var(--teal)" stroke-width="2.4" stroke-linecap="round"><circle cx="18" cy="18" r="7"/><path d="M18 1v5M18 30v5M1 18h5M30 18h5M6 6l3.5 3.5M26.5 26.5L30 30M30 6l-3.5 3.5M9.5 26.5L6 30"/></svg>
  <div class="service-label">AMBULANTE<br>OPERATIONEN</div>
</div>
<div class="service" style="left:143px">
  <svg width="36" height="36" viewBox="0 0 36 36" fill="none" stroke="var(--teal)" stroke-width="2.4" stroke-linecap="round"><circle cx="18" cy="18" r="7"/><path d="M18 1v5M18 30v5M1 18h5M30 18h5M6 6l3.5 3.5M26.5 26.5L30 30M30 6l-3.5 3.5M9.5 26.5L6 30"/></svg>
  <div class="service-label">AMBULANTE<br>OPERATIONEN</div>
</div>
<div class="service" style="left:244px">
  <svg width="36" height="36" viewBox="0 0 36 36" fill="none" stroke="var(--teal)" stroke-width="2.4" stroke-linecap="round"><circle cx="18" cy="18" r="7"/><path d="M18 1v5M18 30v5M1 18h5M30 18h5M6 6l3.5 3.5M26.5 26.5L30 30M30 6l-3.5 3.5M9.5 26.5L6 30"/></svg>
  <div class="service-label">AMBULANTE<br>OPERATIONEN</div>
</div>
<div class="service" style="left:345px">
  <svg width="36" height="36" viewBox="0 0 36 36" fill="none" stroke="var(--teal)" stroke-width="2.4" stroke-linecap="round"><circle cx="18" cy="18" r="7"/><path d="M18 1v5M18 30v5M1 18h5M30 18h5M6 6l3.5 3.5M26.5 26.5L30 30M30 6l-3.5 3.5M9.5 26.5L6 30"/></svg>
  <div class="service-label">AMBULANTE<br>OPERATIONEN</div>
</div>
<div class="service" style="left:447px">
  <svg width="36" height="36" viewBox="0 0 36 36" fill="none" stroke="var(--teal)" stroke-width="2.4" stroke-linecap="round"><circle cx="18" cy="18" r="7"/><path d="M18 1v5M18 30v5M1 18h5M30 18h5M6 6l3.5 3.5M26.5 26.5L30 30M30 6l-3.5 3.5M9.5 26.5L6 30"/></svg>
  <div class="service-label">AMBULANTE<br>OPERATIONEN</div>
</div>
<div class="service" style="left:548px">
  <svg width="36" height="36" viewBox="0 0 36 36" fill="none" stroke="var(--teal)" stroke-width="2.4" stroke-linecap="round"><circle cx="18" cy="18" r="7"/><path d="M18 1v5M18 30v5M1 18h5M30 18h5M6 6l3.5 3.5M26.5 26.5L30 30M30 6l-3.5 3.5M9.5 26.5L6 30"/></svg>
  <div class="service-label">AMBULANTE<br>OPERATIONEN</div>
</div>

<section class="team">
  <h2 class="section-title team-title">UNSER TEAM</h2>
  <p class="team-text">Zusammen mit den 3 Ärzten arbeiten in unserem Team Krankenschwestern und Arzthelfer/innen und eine Orthoptistin, die speziell für diese Aufgaben ausgebildet sind. Sie kümmern sich um ihre augenmedizinischen Probleme und um Ihr Wohlbefinden während der Behandlung.</p>

  <div class="member" style="left:39px;top:117px"><div class="member-photo" role="img" aria-label="Porträtfoto eines Arztes im weißen Kittel"></div><div class="member-name">Prof. Dr Anselm Krauth</div><div class="member-role">Facharzt für Augenheilkunde</div></div>
  <div class="member" style="left:168px;top:117px"><div class="member-photo" role="img" aria-label="Porträtfoto eines Arztes im weißen Kittel"></div><div class="member-name">Prof. Dr Anselm Krauth</div><div class="member-role">Facharzt für Augenheilkunde</div></div>
  <div class="member" style="left:298px;top:117px"><div class="member-photo" role="img" aria-label="Porträtfoto eines Arztes im weißen Kittel"></div><div class="member-name">Prof. Dr Anselm Krauth</div><div class="member-role">Facharzt für Augenheilkunde</div></div>
  <div class="member" style="left:428px;top:117px"><div class="member-photo" role="img" aria-label="Porträtfoto eines Arztes im weißen Kittel"></div><div class="member-name">Prof. Dr Anselm Krauth</div><div class="member-role">Facharzt für Augenheilkunde</div></div>
  <div class="member" style="left:557px;top:117px"><div class="member-photo" role="img" aria-label="Porträtfoto eines Arztes im weißen Kittel"></div><div class="member-name">Prof. Dr Anselm Krauth</div><div class="member-role">Facharzt für Augenheilkunde</div></div>

  <div class="member" style="left:39px;top:270px"><div class="member-photo" role="img" aria-label="Porträtfoto eines Arztes im weißen Kittel"></div><div class="member-name">Prof. Dr Anselm Krauth</div><div class="member-role">Facharzt für Augenheilkunde</div></div>
  <div class="member" style="left:168px;top:270px"><div class="member-photo" role="img" aria-label="Porträtfoto eines Arztes im weißen Kittel"></div><div class="member-name">Prof. Dr Anselm Krauth</div><div class="member-role">Facharzt für Augenheilkunde</div></div>
  <div class="member" style="left:298px;top:270px"><div class="member-photo" role="img" aria-label="Porträtfoto eines Arztes im weißen Kittel"></div><div class="member-name">Prof. Dr Anselm Krauth</div><div class="member-role">Facharzt für Augenheilkunde</div></div>
  <div class="member" style="left:428px;top:270px"><div class="member-photo" role="img" aria-label="Porträtfoto eines Arztes im weißen Kittel"></div><div class="member-name">Prof. Dr Anselm Krauth</div><div class="member-role">Facharzt für Augenheilkunde</div></div>
  <div class="member" style="left:557px;top:270px"><div class="member-photo" role="img" aria-label="Porträtfoto eines Arztes im weißen Kittel"></div><div class="member-name">Prof. Dr Anselm Krauth</div><div class="member-role">Facharzt für Augenheilkunde</div></div>
</section>

</body>
</html>
```